Simple Business Cards for Self-employed Coach

Simple business card with a design that includes the QLT logo.
Using either only the logo color or additional colors that match the logo.

Meridian Guides reach deeply into the past, gathering wisdom from East and West, while still staying current with the frontiers of new discovery in cognitive science, genetics, and other disciplines. see https://www.brightharborpath.example/what-is-integral-coaching/

Target Market(s)

Coaching Clients in Tokyo /Asia; in business organizations, but also outside

Industry/Entity Type

Life Coaching

Contact Information for Business Card

Lukas Brenning
Certified Meridian Guide

3-2-48 Kamiyoshi
Nakarino 164-0392
Tokyo, Japan

Phone: +81 70 4817 5062
E-Mail: lukas.brenning@mailora.example

Font styles to use
Sans Serif

Colors
00a990

Requirements
Must have
• include uploaded logo
• color fitting with QLT logo color
Nice to have
• simple, elegant design
Should not have
• clutter

```html
<!DOCTYPE html>
<html lang="en">
<head>
<meta charset="utf-8">
<title>QLT Business Card – Lukas Brenning</title>
<link rel="stylesheet" href="https://fonts.googleapis.com/css2?family=Questrial&display=swap">
<style>
  :root {
    --brand-teal: #00a990;
    --brand-teal-dark: #0d8f7d;
    --ink: #2b2b2b;
    --card-white: #fbfbfa;
    --stage: #e6e7e7;
  }
  * { box-sizing: border-box; margin: 0; padding: 0; }
  html, body {
    width: 1200px;
    height: 902px;
    overflow: hidden;
    background: var(--stage);
    font-family: "Questrial", "Century Gothic", sans-serif;
  }
  .canvas {
    width: 1200px;
    height: 902px;
    display: flex;
    align-items: center;
    justify-content: center;
  }
  .business-card {
    position: relative;
    width: 1000px;
    height: 572px;
    background: var(--card-white);
    box-shadow: 0 10px 30px rgba(0,0,0,0.15);
    overflow: hidden;
  }
  .corner-tab {
    position: absolute;
    top: 0;
    right: 40px;
    width: 62px;
    height: 26px;
    background: var(--brand-teal);
  }
  .identity {
    position: absolute;
    top: 58px;
    right: 60px;
    text-align: right;
  }
  .identity .person-name {
    font-size: 44px;
    color: var(--brand-teal);
    line-height: 1.1;
  }
  .identity .person-title {
    font-size: 31px;
    color: var(--ink);
    line-height: 1.2;
  }
  .brand-mark {
    position: absolute;
    left: 58px;
    top: 250px;
    display: flex;
    align-items: center;
    gap: 18px;
  }
  .brand-mark .brand-square {
    width: 62px;
    height: 62px;
    background: var(--brand-teal);
  }
  .brand-mark .brand-name {
    font-size: 76px;
    color: var(--brand-teal);
    letter-spacing: 6px;
    line-height: 1;
  }
  .postal-address {
    position: absolute;
    right: 60px;
    top: 330px;
    text-align: right;
    font-size: 31px;
    line-height: 1.4;
    color: var(--brand-teal);
    font-style: normal;
  }
  .contact-band {
    position: absolute;
    left: 0;
    right: 0;
    bottom: 0;
    height: 92px;
    background: linear-gradient(90deg, var(--brand-teal) 0%, var(--brand-teal-dark) 100%);
    display: flex;
    align-items: center;
    justify-content: flex-end;
    padding-right: 60px;
    gap: 26px;
    color: #fff;
    font-size: 31px;
  }
  .contact-band .divider { opacity: 0.9; }
</style>
</head>
<body>
  <main class="canvas">
    <article class="business-card">
      <div class="corner-tab"></div>

      <header class="identity">
        <h1 class="person-name" style="font-weight:400">Lukas Brenning</h1>
        <p class="person-title">Certified Meridian Guide</p>
      </header>

      <div class="brand-mark">
        <span class="brand-square"></span>
        <span class="brand-name">QLT</span>
      </div>

      <address class="postal-address">
        3-2-48 Kamiyoshi Nakarino 164-0392<br>
        Tokyo, Japan
      </address>

      <footer class="contact-band">
        <span class="email">lukas.brenning@mailora.example</span>
        <span class="divider">|</span>
        <span class="phone">+81 70 4817 5062</span>
      </footer>
    </article>
  </main>
</body>
</html>
```